Dunmore Real Estate - Luxury Homes

Create an e-mail template and brochure for a luxury residential home to sell. I want all four photos incorporated in the design.

Target Market(s)

High-net worth individuals.

Industry/Entity Type

Real Estate Agent

Font styles to use
Serif

Colors
000000
757575
c8c8c8

Requirements
Must have
• Think high-fashion ads, minimalism and modern design. In reality, my project is simple, because I only need to have photos and some copy about the house in the template and brochure. The reason I need a designer is to make that information look different from all the other boring marketing you have out there. I would like a one page template I can email out and a two-page brochure.
Nice to have
• I will an award if the idea is really a hit with me and my firm. The award will be $150.
Should not have
• Do not give me a stale, average real estate marketing template campaign.

```html
<!DOCTYPE html>
<html lang="en">
<head>
<meta charset="utf-8">
<title>Harbor Lodge Residence – Dunmore Real Estate</title>
<link rel="stylesheet" href="https://fonts.googleapis.com/css2?family=Raleway:wght@300;400;600&display=swap">
<style>
  :root {
    --backdrop: #2b2b2b;
    --ink-light: #ffffff;
    --panel-dark: rgba(40, 44, 50, 0.55);
    --panel-solid: #3b3b3c;
    --band-green: #0f6a58;
    --forest: #2a3a28;
    --muted: #c8c8c8;
  }
  * { box-sizing: border-box; margin: 0; padding: 0; }
  html, body { width: 1200px; height: 1200px; overflow: hidden; }
  body {
    background: var(--backdrop);
    font-family: "Raleway", sans-serif;
    color: var(--ink-light);
    position: relative;
  }
  .flyer {
    position: absolute; left: 240px; top: 40px;
    width: 716px; height: 1106px;
    background: #1e1e1e; overflow: hidden;
  }
  .photo { position: absolute; }
  .photo-hero {
    left: 0; top: 0; width: 516px; height: 434px;
    background: linear-gradient(180deg, #5d7b4c 0%, #8a6a44 40%, #b07a45 62%, #d8d2c4 76%, #35c0ae 86%, #1f9c8b 100%);
  }
  .photo-grounds {
    left: 516px; top: 0; width: 200px; height: 552px;
    background: linear-gradient(180deg, #1f2a1c 0%, #3c4a2c 45%, #6b5a3c 80%, #8d8270 100%);
  }
  .photo-agent {
    left: 532px; top: 336px; width: 184px; height: 216px;
    background: linear-gradient(180deg, rgba(90,80,60,0) 0%, #34425e 55%, #23304a 100%);
  }
  .photo-kitchen {
    left: 0; top: 554px; width: 410px; height: 552px;
    background: linear-gradient(160deg, #c8762a 0%, #d99a4a 28%, #ece8e2 50%, #b98a5a 75%, #d8d4cf 100%);
  }
  .photo-bath {
    left: 410px; top: 554px; width: 306px; height: 173px;
    background: linear-gradient(90deg, #f2f2f2 0%, #6d6a66 45%, #5a5754 70%, #ededed 100%);
  }
  .photo-living {
    left: 410px; top: 940px; width: 306px; height: 166px;
    background: linear-gradient(90deg, #5f7a55 0%, #efeeea 30%, #f4f2ee 65%, #3e4550 85%, #4a4f58 100%);
  }

  .title-panel {
    position: absolute; left: 0; top: 16px; width: 368px; height: 108px;
    background: var(--panel-dark); padding: 16px 0 0 35px;
  }
  .title-kicker { font-weight: 300; font-size: 20px; line-height: 26px; color: #d8e6d4; }
  .title-name { font-weight: 300; font-size: 27px; line-height: 36px; letter-spacing: .3px; }
  .title-address { font-weight: 400; font-size: 14.5px; line-height: 18px; }

  .price-tag {
    position: absolute; left: 0; top: 142px; width: 184px; height: 41px;
    background: var(--panel-dark); padding-left: 40px;
    font-weight: 300; font-size: 21px; line-height: 41px;
  }

  .brand {
    position: absolute; left: 533px; top: 66px;
    display: flex; align-items: center; gap: 8px;
    font-weight: 400; font-size: 13px; letter-spacing: 2.5px; line-height: 1.2;
  }
  .brand-mark { width: 14px; height: 14px; background: #e08a2c; }

  .details { position: absolute; left: 527px; top: 148px; width: 180px; }
  .details-heading {
    font-weight: 400; font-size: 11.5px; text-decoration: underline;
    text-underline-offset: 2px; margin-left: 26px; margin-bottom: 4px;
  }
  .details-list { list-style: none; font-weight: 300; font-size: 11.5px; line-height: 15.2px; }

  .story-band {
    position: absolute; left: 0; top: 434px; width: 544px; height: 118px;
    background: linear-gradient(90deg, rgba(12,98,80,.92), rgba(15,106,88,.85));
    padding: 10px 0 0 35px;
  }
  .story-text { width: 475px; font-weight: 400; font-size: 11.9px; line-height: 15.2px; }

  .contact {
    position: absolute; left: 532px; top: 458px; width: 184px;
    text-align: center; font-size: 10px; line-height: 13px;
  }
  .contact-label { font-weight: 400; margin-bottom: 3px; }
  .contact-line { font-weight: 600; }

  .renovations {
    position: absolute; left: 410px; top: 730px; width: 306px; height: 206px;
    background: var(--panel-solid); padding: 12px 10px 0 11px;
  }
  .renovations-heading {
    text-align: center; font-weight: 400; font-size: 11.5px;
    text-decoration: underline; text-underline-offset: 2px; margin-bottom: 11px;
  }
  .renovations-list { list-style: none; font-weight: 300; font-size: 11px; line-height: 14px; color: #eeeeee; }
  .renovations-list li { padding-left: 8px; position: relative; }
  .renovations-list li::before { content: "•"; position: absolute; left: 0; }
</style>
</head>
<body>
  <article class="flyer">
    <div class="photo photo-hero" role="img" aria-label="Wood-clad two-storey home with exterior staircase behind a turquoise pool under tropical trees"></div>
    <div class="photo photo-grounds" role="img" aria-label="Shaded tropical garden beside the house"></div>
    <div class="photo photo-agent" role="img" aria-label="Portrait of the listing agent in a navy suit"></div>
    <div class="photo photo-kitchen" role="img" aria-label="Open kitchen and dining room under a vaulted wood-beamed ceiling"></div>
    <div class="photo photo-bath" role="img" aria-label="Master bathroom with grey stone walls, double vanity and freestanding tub"></div>
    <div class="photo photo-living" role="img" aria-label="Bright living room with floor-to-ceiling windows and dark shelving wall"></div>

    <header class="title-panel">
      <p class="title-kicker">For Sale in Coconut Grove</p>
      <h1 class="title-name">HARBOR LODGE RESIDENCE</h1>
      <p class="title-address">1820 HARBOR LODGE DRIVE, MIAMI, FL, 33133</p>
    </header>

    <div class="price-tag">$3,850,000</div>

    <div class="brand"><span class="brand-mark"></span><span>DUNMORE REAL ESTATE</span></div>

    <section class="details">
      <h2 class="details-heading">PROPERTY DETAILS</h2>
      <ul class="details-list">
        <li>4,387 sq. ft. of Total Living Area</li>
        <li>15,563 sq. ft. Lot</li>
        <li>4 Bedrooms</li>
        <li>4 Bathrooms and 2 Half-Baths</li>
        <li>Built in 1987, Renovated in 2016</li>
      </ul>
    </section>

    <section class="story-band">
      <p class="story-text">The ultra-exclusive neighborhood of Camp Biscayne promises a life of utmost privacy and security while being only steps away from the best schools and entertainment Coconut Grove has to offer. This one-of-a-kind home's outdoor and indoor spaces completely restored by Linden Design Studio create a harmonious living space around your tropical oasis. A home full of distinctive details features two oversized master suites, a custom built chef's kitchen, vaulted wood beams, and an outdoor cabana.</p>
    </section>

    <section class="contact">
      <p class="contact-label">FOR SHOWINGS CONTACT</p>
      <p class="contact-line">Julian K. Hartwell</p>
      <p class="contact-line">Tel. 555.214.7080</p>
      <p class="contact-line">julian@dunmore.com</p>
    </section>

    <section class="renovations">
      <h2 class="renovations-heading">RENOVATION IMPROVEMENTS</h2>
      <ul class="renovations-list">
        <li>Additional 1,043 square feet of living area and 340 square feet of terraces created</li>
        <li>Built an outdoor cabana with BBQ grill, summer kitchen, &amp; half bathroom</li>
        <li>Brand-new bathrooms including cabinets, fixtures &amp; flooring</li>
        <li>Installed new windows and doors<br>throughout property</li>
        <li>Brand-new metal roof and brick-paved driveway</li>
        <li>Complete landscape overhaul with new rock beds, putting green, and tree trimming</li>
      </ul>
    </section>
  </article>
</body>
</html>
```